Tolvek Consulting
Tolvek Consulting stationary
Tolvek Consulting - Consulting
Creative Brief
Professional
Daniel R. Tolvek
Chief Executive Officer
Tolvek Consulting, LLC P.O. Box 4372 Phoenix, AZ 85004
daniel@danielrtolvek-mail.com
danielrtolvek-mail.com
Tolvek Consulting Logo

```html
<!DOCTYPE html>
<html lang="en">
<head>
<meta charset="utf-8">
<title>Tolvek Consulting Stationery</title>
<link href="https://fonts.googleapis.com/css2?family=Roboto:wght@400;700;900&display=swap" rel="stylesheet">
<style>
  :root{
    --navy:#0a1a4a;
    --deep:#050d2e;
    --cyan:#19d2f0;
    --blue:#1b6fc4;
    --orange:#f47a1f;
    --red:#e8341c;
    --ink:#1f3b73;
    --grey:#6b6f7a;
    --paper:#ffffff;
    --line:#d9dbe0;
  }
  *{box-sizing:border-box;margin:0;padding:0}
  html,body{width:1200px;height:734px;overflow:hidden;background:var(--paper);font-family:"Roboto",Arial,sans-serif}
  .board{position:relative;width:1200px;height:734px}
  .sheet{position:absolute;background:var(--paper);border:1px solid var(--line);overflow:hidden}
  .brand{display:flex;align-items:center;gap:8px}
  .brand-dot{border-radius:50%;background:var(--orange);flex:none}
  .brand-name{font-weight:900;color:var(--ink);line-height:0.95;text-transform:uppercase;letter-spacing:.5px}
  .brand--light .brand-name{color:#ffffff}

  .letterhead{left:34px;top:31px;width:494px;height:667px}
  .letterhead .brand{position:absolute;left:20px;top:26px}
  .letterhead .brand-dot{width:40px;height:40px}
  .letterhead .brand-name{font-size:21px}
  .letterhead-band{position:absolute;left:0;bottom:0;width:494px;height:120px}
  .letterhead-footer{position:absolute;right:26px;bottom:20px;color:#fff;font-size:8px;line-height:13px;text-align:right}

  .card{position:absolute;width:216px;height:122px;overflow:hidden}
  .card .brand-dot{width:22px;height:22px}
  .card .brand-name{font-size:12px}
  .card-front{left:569px;top:34px;width:230px;height:134px;background:var(--paper);border:1px solid var(--line)}
  .card-front .brand{position:absolute;left:10px;top:12px}
  .card-front .person{position:absolute;left:58px;top:50px;text-align:center;width:110px}
  .person-name{color:var(--orange);font-size:9px;font-weight:700}
  .person-title{color:var(--grey);font-size:6.5px;margin-top:1px}
  .card-contact{position:absolute;right:12px;top:62px;text-align:right;color:var(--grey);font-size:6px;line-height:9px}
  .card-black{left:823px;top:89px;width:219px;height:120px;background:#050505}
  .card-blue{left:526px;top:163px;background:radial-gradient(ellipse at 50% 40%,var(--cyan) 0%,var(--blue) 38%,var(--navy) 75%,var(--deep) 100%)}
  .card-orange{left:701px;top:214px;background:radial-gradient(ellipse at 50% 40%,#ffd23a 0%,var(--orange) 40%,var(--red) 100%)}
  .card-white{left:900px;top:250px;background:var(--paper);border:1px solid var(--line)}
  .card-centre{display:flex;align-items:center;justify-content:center}

  .envelope{left:571px;top:372px;width:605px;height:348px;border:1px solid var(--line)}
  .envelope-flap{position:absolute;left:0;top:0;width:605px;height:110px}
  .envelope-flap-brand{position:absolute;left:280px;top:30px;width:44px;height:44px;border-radius:50%;background:var(--orange)}
  .envelope .return{position:absolute;left:14px;top:122px}
  .envelope .return .brand-dot{width:40px;height:40px}
  .envelope .return .brand-name{font-size:21px}
  .return-address{margin-top:14px;color:var(--ink);font-size:8px;line-height:12px}
  .envelope-band{position:absolute;left:0;bottom:0;width:605px;height:80px}
</style>
</head>
<body>
<main class="board">

  <section class="sheet letterhead" aria-label="Letterhead">
    <div class="brand"><span class="brand-dot"></span><span class="brand-name">Tolvek<br>Consulting</span></div>
    <svg class="letterhead-band" viewBox="0 0 494 120" preserveAspectRatio="none" aria-hidden="true">
      <defs>
        <radialGradient id="lhGlow" cx="0.62" cy="0.8" r="0.7">
          <stop offset="0" stop-color="#19d2f0"/><stop offset="0.45" stop-color="#1b6fc4"/><stop offset="1" stop-color="#0a1a4a"/>
        </radialGradient>
      </defs>
      <path d="M0 40 Q250 8 494 30 L494 120 L0 120Z" fill="#f47a1f"/>
      <path d="M0 46 Q250 16 494 36 L494 120 L0 120Z" fill="#ffffff"/>
      <path d="M0 52 Q250 22 494 42 L494 120 L0 120Z" fill="url(#lhGlow)"/>
    </svg>
    <div class="letterhead-footer">
      Tolvek Consulting, LLC, P.O. Box 4372 Phoenix, AZ 85004<br>
      Cell: 480.555.0139<br>
      daniel@danielrtolvek-mail.com | danielrtolvek-mail.com
    </div>
  </section>

  <section class="sheet card card-front" aria-label="Business card front">
    <div class="brand"><span class="brand-dot"></span><span class="brand-name">Tolvek<br>Consulting</span></div>
    <div class="person"><div class="person-name">Daniel R. Tolvek</div><div class="person-title">Chief Executive Officer</div></div>
    <div class="card-contact">Tolvek Consulting, LLC<br>P.O. Box 4372 Phoenix, AZ 85004<br>Cell: 480.555.0139<br>daniel@danielrtolvek-mail.com<br>danielrtolvek-mail.com</div>
  </section>

  <section class="card card-black card-centre" aria-label="Business card on black">
    <div class="brand brand--light"><span class="brand-dot"></span><span class="brand-name">Tolvek<br>Consulting</span></div>
  </section>

  <section class="card card-blue card-centre" aria-label="Business card on blue">
    <div class="brand brand--light"><span class="brand-dot"></span><span class="brand-name">Tolvek<br>Consulting</span></div>
  </section>

  <section class="card card-orange card-centre" aria-label="Business card on orange">
    <div class="brand brand--light"><span class="brand-dot" style="background:#ffffff"></span><span class="brand-name">Tolvek<br>Consulting</span></div>
  </section>

  <section class="card card-white card-centre" aria-label="Business card on white">
    <div class="brand"><span class="brand-dot"></span><span class="brand-name">Tolvek<br>Consulting</span></div>
  </section>

  <section class="sheet envelope" aria-label="Envelope">
    <svg class="envelope-flap" viewBox="0 0 605 110" preserveAspectRatio="none" aria-hidden="true">
      <defs>
        <radialGradient id="flapGlow" cx="0.5" cy="0.5" r="0.5">
          <stop offset="0" stop-color="#19d2f0"/><stop offset="0.3" stop-color="#1b6fc4"/><stop offset="1" stop-color="#0a1a4a"/>
        </radialGradient>
      </defs>
      <path d="M0 0 H605 V40 Q302 118 0 40Z" fill="url(#flapGlow)"/>
    </svg>
    <span class="envelope-flap-brand"></span>
    <div class="return">
      <div class="brand"><span class="brand-dot"></span><span class="brand-name">Tolvek<br>Consulting</span></div>
      <div class="return-address">Tolvek Consulting<br>LLC, P.O. Box 4372 Phoenix, AZ 85004</div>
    </div>
    <svg class="envelope-band" viewBox="0 0 605 80" preserveAspectRatio="none" aria-hidden="true">
      <defs>
        <radialGradient id="envGlow" cx="0.55" cy="0.9" r="0.7">
          <stop offset="0" stop-color="#19d2f0"/><stop offset="0.45" stop-color="#1b6fc4"/><stop offset="1" stop-color="#0a1a4a"/>
        </radialGradient>
      </defs>
      <path d="M0 22 Q300 0 605 16 L605 80 L0 80Z" fill="#f47a1f"/>
      <path d="M0 28 Q300 6 605 22 L605 80 L0 80Z" fill="#ffffff"/>
      <path d="M0 34 Q300 12 605 28 L605 80 L0 80Z" fill="url(#envGlow)"/>
    </svg>
  </section>

</main>
</body>
</html>
```